Text only wordpress site to capture emails

Refer to inspiration upload for list of sites that will be useful for you.

We need a site that will be used to capture emails from clients that follow us on social media. The site will be all text, pretty simple. I have a couple of text sites that I like and we can use them for an example.

Menu section will have home, archive, about.
Footer will have © and Website Privacy Policy | Legal and Policies
There will be some text on the home page and an email capture.

This site will be all text no pictures.

I discuss Cubicle Chatter so the text portions will have some questions and answers on this and then prompt for the visitor to subscribe to my email list.

The only purpose of the site is to build an email list from existing social media followers so the site will be pretty simple in and of itself.

• Text only, similar Q&A to uploaded pics.

I will use a template from letter pinecone dotcom for email capture.

I like the simple couriernew font family that is on both sites supplied in the uploads.
• If you use any color it needs to be very minimal.

```html
<!DOCTYPE html>
<html lang="en">
<head>
<meta charset="utf-8">
<title>Cubicle Chatter</title>
<link href="https://fonts.googleapis.com/css2?family=Courier+Prime:wght@400;700&display=swap" rel="stylesheet">
<style>
  :root {
    --ink: #111111;
    --text: #4a4a4a;
    --muted: #555555;
    --rule: #cfcfcf;
    --field-border: #cccccc;
    --button: #e6e6e6;
    --paper: #ffffff;
  }
  * { box-sizing: border-box; margin: 0; padding: 0; }
  html, body {
    width: 1074px; height: 1200px; overflow: hidden;
    background: var(--paper);
    font-family: "Courier Prime", "Courier New", monospace;
    color: var(--text);
  }
  .page { width: 822px; margin: 0 auto; position: relative; height: 1200px; }

  .site-header {
    height: 81px; border-bottom: 1px dashed var(--rule);
    display: flex; justify-content: space-between; align-items: center;
    padding-top: 2px;
  }
  .site-title { font-weight: 400; font-size: 27px; color: var(--ink); letter-spacing: 0.6px; margin-left: 2px; margin-top: -4px; }
  .main-nav { display: flex; gap: 41px; margin-top: -6px; }
  .main-nav a { color: var(--ink); text-decoration: none; font-size: 13px; letter-spacing: 0.3px; }

  .content { display: grid; grid-template-columns: 316px 444px; column-gap: 62px; padding-top: 51px; }

  .signup h2 { font-weight: 400; font-size: 24px; color: var(--ink); letter-spacing: 0.7px; margin-left: 2px; line-height: 1.2; }
  .signup p { font-size: 11px; line-height: 16px; letter-spacing: 0.35px; margin: 7px 0 0 2px; width: 306px; }
  .email-field {
    margin-top: 23px; height: 35px; border: 1px solid var(--field-border); border-radius: 2px;
    display: flex; align-items: center; padding-left: 13px; gap: 6px;
    font-size: 11px; letter-spacing: 0.35px; color: var(--muted);
  }
  .email-field svg { width: 12px; height: 10px; }
  .subscribe-button {
    margin-top: 18px; width: 126px; height: 35px; border: 0; border-radius: 3px;
    background: var(--button); font-family: inherit; font-weight: 700; font-size: 12px; color: var(--ink);
  }

  .qa-intro h2 { font-size: 14px; font-weight: 700; color: var(--ink); letter-spacing: 1px; margin-top: 2px; }
  .qa-intro p { font-size: 11px; letter-spacing: 0.35px; margin-top: 9px; }
  .qa-list { list-style: none; margin-top: 18px; }
  .qa-item { border-bottom: 1px dashed var(--rule); padding: 19px 0 18px; }
  .qa-item:first-child { padding-top: 16px; }
  .qa-item:last-child { border-bottom: 0; }
  .question { display: flex; align-items: center; gap: 7px; font-size: 11px; font-weight: 700; color: var(--ink); letter-spacing: 0.35px; }
  .question svg { width: 13px; height: 11px; flex: none; }
  .answer { font-size: 11px; line-height: 16px; letter-spacing: 0.35px; margin-top: 7px; }
  .answer b { color: var(--ink); }

  .site-footer {
    position: absolute; top: 1124px; left: 0; right: 0;
    border-top: 1px dashed var(--rule);
    display: flex; justify-content: space-between; padding-top: 20px;
  }
  .legal { font-size: 11px; letter-spacing: 0.35px; line-height: 20px; margin-left: 2px; }
  .follow { display: flex; align-items: center; gap: 9px; font-size: 11px; letter-spacing: 0.35px; margin-top: 3px; }
  .follow span { margin-right: 1px; }
  .social-link {
    width: 28px; height: 28px; background: var(--button); border-radius: 2px;
    display: flex; align-items: center; justify-content: center;
    font-size: 7.5px; font-weight: 700; color: var(--ink); text-decoration: none;
  }
</style>
</head>
<body>
<div class="page">
  <header class="site-header">
    <h1 class="site-title">Cubicle Chatter</h1>
    <nav class="main-nav">
      <a href="#">Home</a>
      <a href="#">Archive</a>
      <a href="#">About Us</a>
    </nav>
  </header>

  <main class="content">
    <section class="signup">
      <h2>Newsletter Signup</h2>
      <p>Ut wisi enim ad minim veniam, quis nostrud exerci tation ullamcorper suscipit lobortis nisl ut aliquip ex ea commodo consequat.</p>
      <div class="email-field">
        <svg viewBox="0 0 12 10" aria-hidden="true"><rect x="0" y="0" width="12" height="10" rx="1.2" fill="#111"/><path d="M0.8 1.2 L6 5.2 L11.2 1.2" stroke="#fff" stroke-width="1.1" fill="none"/></svg>
        Enter Your Email
      </div>
      <button class="subscribe-button">Subscribe</button>
    </section>

    <section class="qa">
      <div class="qa-intro">
        <h2>What the...</h2>
        <p>Lorem ipsum dolor sit amet, consectetuer adipiscing elit.</p>
      </div>
      <ul class="qa-list">
        <li class="qa-item"><div class="question"><svg viewBox="0 0 13 11"><path d="M1 1l4.5 4.5L1 10M6 1l4.5 4.5L6 10" stroke="#111" stroke-width="1.3" fill="none"/></svg>Ut wisi enim ad minim veniam</div><p class="answer"><b>A:</b>Lorem ipsum dolor sit amet, consectetuer adipiscing elit, sed diam nonummy nibh euismod tincidunt ut laoreet dolorena aliquam erat volutpat. Ut wisi enim ad minim veniam quis.</p></li>
        <li class="qa-item"><div class="question"><svg viewBox="0 0 13 11"><path d="M1 1l4.5 4.5L1 10M6 1l4.5 4.5L6 10" stroke="#111" stroke-width="1.3" fill="none"/></svg>Sed diam nonummy nibh euismod</div><p class="answer"><b>A:</b>Lorem ipsum dolor sit amet, consectetuer adipiscing elit, sed diam nonummy nibh euismod tincidunt ut laoreet dolorena aliquam erat volutpat. Ut wisi enim ad minim veniam quis.</p></li>
        <li class="qa-item"><div class="question"><svg viewBox="0 0 13 11"><path d="M1 1l4.5 4.5L1 10M6 1l4.5 4.5L6 10" stroke="#111" stroke-width="1.3" fill="none"/></svg>Duis autem vel eum iriure dolor in hendrerit</div><p class="answer"><b>A:</b>Lorem ipsum dolor sit amet, consectetuer adipiscing elit, sed diam nonummy nibh euismod tincidunt ut laoreet.</p></li>
        <li class="qa-item"><div class="question"><svg viewBox="0 0 13 11"><path d="M1 1l4.5 4.5L1 10M6 1l4.5 4.5L6 10" stroke="#111" stroke-width="1.3" fill="none"/></svg>Sed diam nonummy nibh euismod</div><p class="answer"><b>A:</b>Lorem ipsum dolor sit amet, consectetuer adipiscing elit, sed diam nonummy nibh euismod tincidunt ut laoreet dolorena aliquam erat volutpat. Ut wisi enim ad minim veniam quis.</p></li>
        <li class="qa-item"><div class="question"><svg viewBox="0 0 13 11"><path d="M1 1l4.5 4.5L1 10M6 1l4.5 4.5L6 10" stroke="#111" stroke-width="1.3" fill="none"/></svg>Ut wisi enim ad minim veniam</div><p class="answer"><b>A:</b>Lorem ipsum dolor sit amet, consectetuer adipiscing elit, sed diam nonummy nibh euismod tincidunt ut laoreet dolorena aliquam erat volutpat. Ut wisi enim ad minim veniam quis.</p></li>
        <li class="qa-item"><div class="question"><svg viewBox="0 0 13 11"><path d="M1 1l4.5 4.5L1 10M6 1l4.5 4.5L6 10" stroke="#111" stroke-width="1.3" fill="none"/></svg>Duis autem vel eum iriure dolor in hendrerit</div><p class="answer"><b>A:</b>Lorem ipsum dolor sit amet, consectetuer adipiscing elit, sed diam nonummy nibh euismod tincidunt ut laoreet.</p></li>
        <li class="qa-item"><div class="question"><svg viewBox="0 0 13 11"><path d="M1 1l4.5 4.5L1 10M6 1l4.5 4.5L6 10" stroke="#111" stroke-width="1.3" fill="none"/></svg>Sed diam nonummy nibh euismod</div><p class="answer"><b>A:</b>Lorem ipsum dolor sit amet, consectetuer adipiscing elit, sed diam nonummy nibh euismod tincidunt ut laoreet dolorena aliquam erat volutpat. Ut wisi enim ad minim veniam quis.</p></li>
        <li class="qa-item"><div class="question"><svg viewBox="0 0 13 11"><path d="M1 1l4.5 4.5L1 10M6 1l4.5 4.5L6 10" stroke="#111" stroke-width="1.3" fill="none"/></svg>Ut wisi enim ad minim veniam</div><p class="answer"><b>A:</b>Lorem ipsum dolor sit amet, consectetuer adipiscing elit, sed diam nonummy nibh euismod tincidunt ut laoreet dolorena aliquam erat volutpat. Ut wisi enim ad minim veniam quis.</p></li>
        <li class="qa-item"><div class="question"><svg viewBox="0 0 13 11"><path d="M1 1l4.5 4.5L1 10M6 1l4.5 4.5L6 10" stroke="#111" stroke-width="1.3" fill="none"/></svg>Duis autem vel eum iriure dolor in hendrerit</div><p class="answer"><b>A:</b>Lorem ipsum dolor sit amet, consectetuer adipiscing elit, sed diam nonummy nibh euismod tincidunt ut laoreet.</p></li>
      </ul>
    </section>
  </main>

  <footer class="site-footer">
    <div class="legal">
      <p>Copyright © 2021 Cubicle Chatter. All Right Reserved.</p>
      <p>Privacy Policy | Legal and Policies</p>
    </div>
    <div class="follow">
      <span>Follow Us:</span>
      <a class="social-link" href="#">Pals</a>
      <a class="social-link" href="#">Pics</a>
      <a class="social-link" href="#">Chirp</a>
    </div>
  </footer>
</div>
</body>
</html>
```